Steel Company / Iron Railing Business Card Template

We are a custom steel fabrication company located in Hollis Ferry, OH. In business since 1979, we recently developed a new logo, and we're looking for a business card design to help display the new logo and our business. The name of the company is Kelbrook Forge Co.. The Office Phone number is (610) 555-0143. We fabricate and install custom "wrought iron" railings on our residential side, we also fabricate and erect structural steel (think cranes and steel beams in buildings) on our commercial side. Looking to get a business card template designed. Something modern, but professional. Clear and easy to read. Front should have all business and employee information including phone number(s), email address, business information, etc. back should spotlight logo.

Industry/Entity Type

Construction / Home Improvement

Contact Information for Business Card

Business information is Kelbrook Forge Co., 48 Dunmore Ave Suite 3305, Hollis Ferry, OH 19074. Phone number is (610) 555-0143. Website is www.kelbrookforge.example Business card should be for "Tom Pelling" with the job title "Sales & Estimating" but be editable for other employees. Tom's phone number is (610) 555-0178

Colors

Designer to choose colors to be used in the design.

Requirements
Must have
• Modern Feel, Design should be sized for standard business card sizing 3.5" x 2" (88.9mm x 50.8mm)

```html
<!DOCTYPE html>
<html lang="en">
<head>
<meta charset="utf-8">
<title>Kelbrook Forge Co. — Business Card</title>
<link rel="stylesheet" href="https://fonts.googleapis.com/css2?family=Lato:wght@400;700;900&display=swap">
<style>
  :root {
    --stage: #2a2a2c;
    --brand-blue: #25418d;
    --brand-red: #d0232b;
    --card-white: #ffffff;
    --ink: #1f1f1f;
    --radius: 18px;
  }
  * { box-sizing: border-box; margin: 0; padding: 0; }
  html, body {
    width: 1200px; height: 875px; overflow: hidden;
    background: var(--stage);
    font-family: "Lato", sans-serif;
  }
  .stage { position: relative; width: 1200px; height: 875px; }

  .card {
    position: absolute; left: 300px;
    width: 600px; height: 343px;
    border-radius: var(--radius);
    overflow: hidden;
  }

  /* Back: logo spotlight */
  .card--back { top: 54px; background: var(--brand-blue); display: flex; align-items: center; justify-content: center; }
  .brand-mark { display: flex; align-items: center; gap: 16px; }
  .brand-mark__dot { width: 22px; height: 22px; border-radius: 50%; background: var(--brand-red); }
  .brand-mark__name { color: var(--card-white); font-weight: 900; font-size: 40px; letter-spacing: 1px; }

  /* Front: contact details */
  .card--front { top: 478px; background: var(--card-white); }
  .card__art { position: absolute; inset: 0; }

  .contact { position: absolute; left: 52px; top: 82px; }
  .contact__name { color: var(--brand-blue); font-weight: 900; font-size: 30px; letter-spacing: 0.5px; text-transform: uppercase; line-height: 1; }
  .contact__title { color: var(--brand-red); font-size: 15px; margin-top: 6px; }
  .contact__rule { width: 38px; height: 3px; background: var(--brand-blue); margin: 14px 0 14px; }
  .contact__list { list-style: none; }
  .contact__item { display: flex; gap: 10px; font-size: 12.5px; color: var(--ink); line-height: 17px; }
  .contact__icon { width: 12px; height: 17px; flex: none; display: flex; align-items: center; }
  .contact__icon svg { width: 12px; height: 12px; fill: var(--brand-red); }
  .contact__icon .icon-globe { fill: none; stroke: var(--brand-red); stroke-width: 1.2; }
  .contact__company { font-weight: 700; }
</style>
</head>
<body>
<main class="stage">

  <section class="card card--back" aria-label="Card back">
    <div class="brand-mark">
      <span class="brand-mark__dot"></span>
      <span class="brand-mark__name">Kelbrook Forge Co.</span>
    </div>
  </section>

  <section class="card card--front" aria-label="Card front">
    <svg class="card__art" viewBox="0 0 600 343" width="600" height="343">
      <defs>
        <linearGradient id="railing-tone" x1="0" y1="0" x2="1" y2="1">
          <stop offset="0" stop-color="#25418d"/>
          <stop offset="1" stop-color="#5a76c0"/>
        </linearGradient>
      </defs>
      <polygon class="corner-band" points="400,0 600,0 600,40 340,40" fill="#d0232b"/>
      <polygon role="img" aria-label="Wrought iron stair railing illustration"
               points="330,58 600,50 600,200 450,262 420,262 420,170 330,110"
               fill="url(#railing-tone)"/>
    </svg>

    <div class="contact">
      <h1 class="contact__name">Tom Pelling</h1>
      <p class="contact__title">Sales &amp; Estimating</p>
      <div class="contact__rule"></div>
      <ul class="contact__list">
        <li class="contact__item">
          <span class="contact__icon"><svg viewBox="0 0 12 12"><path d="M6 0a4 4 0 0 0-4 4c0 3 4 8 4 8s4-5 4-8a4 4 0 0 0-4-4zm0 5.5A1.5 1.5 0 1 1 6 2.5a1.5 1.5 0 0 1 0 3z"/></svg></span>
          <span><span class="contact__company">Kelbrook Forge Co.</span><br>48 Dunmore Ave Suite 3305<br>Hollis Ferry, OH 19074</span>
        </li>
        <li class="contact__item">
          <span class="contact__icon"><svg viewBox="0 0 12 12"><path d="M2.5 0.5l2 2.5-1 1.5c.8 1.6 2 2.8 3.5 3.5l1.5-1 2.5 2-1 2.5C5 11 1 7 0.5 2z"/></svg></span>
          <span>(610) 555-0143</span>
        </li>
        <li class="contact__item">
          <span class="contact__icon"><svg viewBox="0 0 12 12"><path d="M3 0h6a1 1 0 0 1 1 1v10a1 1 0 0 1-1 1H3a1 1 0 0 1-1-1V1a1 1 0 0 1 1-1zm0 1.5v8h6v-8z"/></svg></span>
          <span>(610) 555-0178</span>
        </li>
        <li class="contact__item">
          <span class="contact__icon"><svg viewBox="0 0 12 12"><path d="M0 2h12v8H0zm1 1v.3l5 3.2 5-3.2V3z"/></svg></span>
          <span>tpelling@kelbrookforge.example</span>
        </li>
        <li class="contact__item">
          <span class="contact__icon"><svg viewBox="0 0 12 12"><path d="M0 2h12v8H0zm1 1v.3l5 3.2 5-3.2V3z"/></svg></span>
          <span>info@kelbrookforge.example</span>
        </li>
        <li class="contact__item">
          <span class="contact__icon"><svg viewBox="0 0 12 12" class="icon-globe"><circle cx="6" cy="6" r="5.2"/><ellipse cx="6" cy="6" rx="2.3" ry="5.2"/><path d="M0.8 6h10.4"/></svg></span>
          <span>www.kelbrookforge.example</span>
        </li>
      </ul>
    </div>
  </section>

</main>
</body>
</html>
```